依頼詳細
■デザインに期待すること
・いわゆる漢方というイメージではなく、シンプルでおしゃれなデザインにしたいです。
・理由は、ユーザーに漢方という特別なイメージを持たせない、敷居を下げ足を運びやすくしたいと考えているからです。
・奇抜ではなく、化粧品会社などスタイリッシュなイメージです。
・キャッチコピーは「頑張ってるけど結果が出ない方へ」です。
ページ数
1ページ
希望イメージ
シンプル 複雑
単色 カラフル
暗い 明るい
日常 高級
遊び心 厳粛
未来的 伝統的
女性的 男性的
希望する色
茶系、無彩色系、ベージュ系
納品ファイル
• 高解像度JPG (.jpg)
• イラストレーター形式 (.ai)
• フォトショップ形式 (.psd)
• PNG形式 (.png)

```html
<!DOCTYPE html>
<html lang="ja">
<head>
<meta charset="UTF-8">
<title>〇〇漢方堂</title>
<link rel="stylesheet" href="https://fonts.googleapis.com/css2?family=Cormorant+Garamond:wght@400;500&family=Noto+Serif+JP:wght@400;500;600&family=Noto+Sans+JP:wght@300;400&display=swap">
<style>
:root{
  --ink:#2f2925;
  --ink-soft:#6f6660;
  --line:#b9b0a8;
  --beige:#f3eee8;
  --beige-deep:#ebe3da;
  --white:#ffffff;
}
*{margin:0;padding:0;box-sizing:border-box}
html,body{width:1200px;height:5192px;overflow:hidden;background:var(--white)}
body{position:relative;color:var(--ink);font-family:"Noto Sans JP",sans-serif}
.abs{position:absolute}
.en{font-family:"Cormorant Garamond",serif;font-weight:400;letter-spacing:.04em}
.jp-serif{font-family:"Noto Serif JP",serif}
.fill{position:absolute}
.vline{position:absolute;width:1px;background:var(--ink)}

/* header */
.site-header{position:absolute;left:0;top:0;width:1200px;height:64px;z-index:5;background:rgba(255,255,255,.85)}
.logo{position:absolute;left:26px;top:18px;font-family:"Noto Serif JP",serif;font-size:22px;font-weight:600;letter-spacing:.06em}
.header-tag{position:absolute;left:180px;top:26px;font-size:11px;color:var(--ink-soft)}
.social{position:absolute;display:flex;gap:10px}
.social span{width:22px;height:22px;border-radius:50%;background:var(--ink-soft);display:block}
.menu{position:absolute;right:42px;top:24px;width:50px}
.menu i{display:block;height:1px;background:var(--ink);margin-bottom:9px}

/* hero */
.hero-photo{left:0;top:0;width:1200px;height:1380px;background:linear-gradient(160deg,#f4efe9 0%,#e9dccb 30%,#d8bfa0 55%,#e6d4bd 80%,#f1ebe4 100%)}
.catch{left:0;width:1200px;top:712px;text-align:center;font-family:"Noto Serif JP",serif;font-size:32px;font-weight:600;letter-spacing:.12em;color:var(--ink)}
.catch span{background:rgba(255,255,255,.85);padding:4px 18px}
.scroll{left:912px;top:1220px;writing-mode:vertical-rl;font-size:12px;letter-spacing:.2em;color:var(--ink)}
.dots{left:650px;top:1336px;display:flex;gap:56px}
.dots i{width:9px;height:9px;border-radius:50%;background:var(--line);display:block}
.dots i:first-child{background:var(--ink)}

/* section heads */
.head-box{position:absolute;background:var(--white);padding:30px 40px}
.head-title{font-family:"Cormorant Garamond",serif;font-size:72px;line-height:1;letter-spacing:.03em}
.head-sub{font-family:"Noto Serif JP",serif;font-size:13px;font-weight:600;margin-top:10px}

/* link rows */
.link-row{position:absolute;width:390px}
.link-row p{font-size:12px;color:var(--ink-soft);margin-bottom:12px}
.link-row svg{display:block}
.more{position:absolute;font-size:10px;letter-spacing:.16em;color:var(--ink-soft);border-bottom:1px solid var(--line);width:200px;padding-bottom:8px}
.note{position:absolute;font-size:12px;color:var(--ink-soft);line-height:2.3}

/* news */
.news-row{position:absolute;left:240px;width:720px;display:flex;font-size:12px;color:var(--ink-soft);border-bottom:1px solid var(--line);padding-bottom:10px}
.news-row .date{width:140px}
.news-row .cat{width:160px}

/* footer */
.footer{left:0;top:4940px;width:1200px;height:252px;background:var(--beige)}
.foot-nav{position:absolute;display:flex;gap:56px;font-size:10px;color:var(--ink-soft)}
</style>
</head>
<body>

<header class="site-header">
  <div class="logo">〇〇漢方堂</div>
  <div class="header-tag">漢方相談、ケミカル、その場での漢方をお届けいたします</div>
  <div class="social" style="left:800px;top:20px"><span></span><span></span><span></span></div>
  <div class="menu"><i></i><i></i></div>
</header>

<!-- hero -->
<div class="fill hero-photo" role="img" aria-label="白い器に盛られた様々な生薬の写真"></div>
<div class="abs catch"><span>頑張っているけど、結果が出ない方へ</span></div>
<div class="abs scroll en">scroll down</div>
<div class="abs dots"><i></i><i></i><i></i><i></i></div>

<!-- reason -->
<div class="fill" style="left:140px;top:1380px;width:920px;height:580px;background:var(--beige)"></div>
<div class="fill" style="left:140px;top:1380px;width:452px;height:580px;background:linear-gradient(160deg,#efe9e2,#e6c277 45%,#e0a72a 55%,#d9cfc4)" role="img" aria-label="スパイスをすくった木のスプーンの写真"></div>
<div class="abs jp-serif" style="left:356px;top:1440px;writing-mode:vertical-rl;font-size:24px;font-weight:600;line-height:1.7;letter-spacing:.1em">ここにテキストが入る<br>ここにテキストが入る</div>
<div class="head-box" style="left:592px;top:1312px;width:456px;height:228px">
  <div class="head-title" style="margin-top:20px">REASON</div>
  <div class="head-sub">漢方先生が選ばれる理由</div>
</div>
<div class="link-row" style="left:620px;top:1670px"><p>ここにテキストが入ります</p><svg width="370" height="12"><path d="M0 10H368L356 2" fill="none" stroke="#2f2925"/></svg></div>
<div class="link-row" style="left:620px;top:1760px"><p>ここにテキストが入ります</p><svg width="370" height="12"><path d="M0 10H368L356 2" fill="none" stroke="#2f2925"/></svg></div>
<div class="link-row" style="left:620px;top:1850px"><p>ここにテキストが入ります</p><svg width="370" height="12"><path d="M0 10H368L356 2" fill="none" stroke="#2f2925"/></svg></div>
<div class="vline" style="left:232px;top:1940px;height:160px"></div>

<!-- choice -->
<div class="fill" style="left:140px;top:2120px;width:420px;height:440px;background:var(--beige)"></div>
<div class="fill" style="left:488px;top:2140px;width:452px;height:420px;background:linear-gradient(135deg,#6a4430,#8a5c3e 50%,#5a3826)" role="img" aria-label="漢方薬の引き出し棚の写真"></div>
<div class="head-box" style="left:190px;top:2110px;width:300px;background:transparent;padding:30px 30px">
  <div class="head-title" style="font-size:60px">CHOICE</div>
  <div class="head-sub">漢方薬局の選び方</div>
</div>
<div class="note" style="left:230px;top:2355px">ここにテキストが入ります<br>ここにテキストが入ります</div>
<div class="more" style="left:230px;top:2474px">VIEW MORE</div>
<div class="vline" style="left:960px;top:2600px;height:160px"></div>

<!-- consult -->
<div class="fill" style="left:640px;top:2760px;width:408px;height:440px;background:var(--beige)"></div>
<div class="fill" style="left:140px;top:2760px;width:500px;height:440px;background:linear-gradient(120deg,#e9e3dc,#d8cfc6 50%,#f1ece6)" role="img" aria-label="窓辺で膝を抱えて座る女性の写真"></div>
<div class="head-box" style="left:640px;top:2770px;width:380px;background:transparent;padding:20px 30px">
  <div class="head-title" style="font-size:60px">CONSULT</div>
  <div class="head-sub">ホンカミモ気軽でお悩みの方へ</div>
</div>
<div class="note" style="left:700px;top:2985px">ここにテキストが入ります<br>ここにテキストが入ります</div>
<div class="more" style="left:700px;top:3110px">VIEW MORE</div>
<div class="vline" style="left:232px;top:3220px;height:180px"></div>

<!-- flow -->
<div class="fill" style="left:140px;top:3320px;width:460px;height:460px;background:var(--beige)"></div>
<div class="fill" style="left:488px;top:3420px;width:532px;height:408px;background:linear-gradient(135deg,#d8dbde,#f2f2f2 45%,#bfc3c6)" role="img" aria-label="パソコンの前でカウンセリングする手元の写真"></div>
<div class="head-box" style="left:190px;top:3390px;width:300px;background:transparent;padding:30px 30px">
  <div class="head-title" style="font-size:60px">FLOW</div>
  <div class="head-sub">カウンセリングの流れ</div>
</div>
<div class="note" style="left:230px;top:3610px">ここにテキストが入ります<br>ここにテキストが入ります</div>
<div class="more" style="left:230px;top:3730px">VIEW MORE</div>
<div class="vline" style="left:960px;top:3820px;height:140px"></div>

<!-- shop -->
<div class="abs" style="left:640px;top:3920px">
  <div class="head-title" style="font-size:60px;text-align:right;padding-right:60px">SHOP</div>
  <div class="head-sub" style="font-size:12px;margin-top:8px">オンラインショップもお気軽にご利用いただけます</div>
</div>
<div class="fill" style="left:260px;top:4030px;width:788px;height:136px;background:linear-gradient(90deg,#f6f3ef,#f3e7c8 45%,#f0d86a 60%,#f4eee8)" role="img" aria-label="サプリメントやカプセルが並ぶ写真"></div>

<!-- news -->
<div class="fill" style="left:100px;top:4190px;width:948px;height:340px;background:var(--beige)"></div>
<div class="abs en" style="left:100px;top:4260px;writing-mode:vertical-rl;font-size:64px;letter-spacing:.06em">NEWS</div>
<div class="news-row" style="top:4262px"><span class="date">2020.10.01</span><span class="cat">category</span><span>ここにテキストが入ります</span></div>
<div class="news-row" style="top:4322px"><span class="date">2020.10.01</span><span class="cat">category</span><span>ここにテキストが入ります</span></div>
<div class="news-row" style="top:4382px"><span class="date">2020.10.01</span><span class="cat">category</span><span>ここにテキストが入ります</span></div>
<div class="news-row" style="top:4442px"><span class="date">2020.10.01</span><span class="cat">category</span><span>ここにテキストが入ります</span></div>
<div class="more" style="left:240px;top:4492px;border:none">VIEW MORE</div>

<!-- access -->
<div class="note" style="left:240px;top:4600px;line-height:2">address<br>〒000-0000<br>東京都〇〇区〇〇 1-2-3<br><br>営業 10:00〜19:00</div>
<div class="abs" style="left:240px;top:4770px;display:flex;gap:24px">
  <svg width="40" height="40"><circle cx="20" cy="20" r="19" fill="none" stroke="#b9b0a8"/><path d="M14 13c0 8 5 14 13 14l2-4-4-2-2 2c-3-1-5-3-6-6l2-2-2-4z" fill="none" stroke="#6f6660"/></svg>
  <svg width="40" height="40"><circle cx="20" cy="20" r="19" fill="none" stroke="#b9b0a8"/><path d="M20 30s-7-8-7-13a7 7 0 0 1 14 0c0 5-7 13-7 13z" fill="none" stroke="#6f6660"/><circle cx="20" cy="17" r="2.5" fill="#6f6660"/></svg>
</div>
<div class="fill" style="left:600px;top:4560px;width:420px;height:360px;background:linear-gradient(135deg,#e8ecef,#dfe7dc 50%,#eae6df)" role="img" aria-label="店舗周辺の地図"></div>

<!-- footer -->
<div class="fill footer"></div>
<div class="abs jp-serif" style="left:240px;top:4990px;font-size:14px;font-weight:500;line-height:1.8">キャッチコピーキャッチコピー<br>キャッチコピー</div>
<div class="abs" style="left:240px;top:5100px;font-family:'Noto Serif JP',serif;font-size:18px;font-weight:600">〇〇漢方堂</div>
<div class="foot-nav" style="top:5048px;left:470px"><span>TOP</span><span>REASON</span><span>CHOICE</span><span>CONSULT</span><span>SHOP</span></div>
<div class="abs en" style="left:700px;top:5082px;font-size:22px">follow us</div>
<div class="abs" style="left:805px;top:5096px;width:80px;height:1px;background:var(--ink)"></div>
<div class="social" style="left:895px;top:5082px"><span></span><span></span><span></span></div>

</body>
</html>
```